Flyer-Design für Zweithaar Studio
Zielgruppe
Firma MOLVA Ketz ist ein Zweithaar Studio. Hier erhalten Kunden individuell auf sie zugeschnittene Perücken und Toupets. Unsere Zielgruppe sind Männer und Frauen mit wenig oder keiner Kopfbehaarung oder Menschen die krankheitsbedingt unter Haarausfall leiden.
Aufgabenstellung
Bitte Vorschläge zu Anzahl Seiten und Format erstellen, aktuell haben wir noch keine Vorstellung dazu. Folgende Inhalte haben wir schon mal als Entwurf vorbereitet:
Eine Seite zum Thema Toupets mit dem Bild vom Mann:
Leiden Sie an übermäßigem Haarausfall?
Fühlen Sie sich nicht mehr 100% wohl damit und möchten gerne wieder Ihre Attraktivität und vor allem das Wohlbefinden steigern?
Dann sind Sie bei uns sehr gut aufgehoben, denn wir können Ihnen Ihr Toupet individuell auf Ihre Bedürfnisse hin z.B. Farbe, Grauanteil, Größe und Styling anpassen.
Eine Seite zum Thema Perücken mit dem Bild der Frau:
Sind Sie an einer Perücke interessiert die augenscheinlich keinen Unterschied zu gewachsenem Haar aufweist?
Dann sind Sie bei uns an der richtigen Adresse. Die langjährige Erfahrung im Zweithaar Bereich von Friseurmeisterin verspricht Ihnen optimale Beratung und ein individuell auf Sie abgestimmtes Produkt.
Bei uns erhalten Sie Zugriff auf verschiedene Modelle im gesamten Preisspektrum.
Liegt eine von Ihrem Arzt attestierte Erkrankung vor, übernimmt Ihre Krankenkasse höchstwahrscheinlich die Kosten für Ihr Zweithaar. Die Formalitäten dazu erledigen wir gerne für Sie um Ihnen unnötigen Stress zu ersparen.
Eine weitere Seite mit den besonderen Merkmalen mit dem Bild Diversity:
Mit unserer Befestigungsmethode sind Sie sehr flexibel - starker halt für jede Situation und auf Wunsch auch abnehmbar z.B. nachts beim schlafen.
Der große Vorteil unserer Befestigungsmethode liegt darin, dass Sie diese selbst umsetzen können und somit nicht jeden Monat das Studio zur Neubefestigung aufsuchen müssen. Das spart Ihnen Zeit und Geld.
Wir können Ihnen Toupets und Perücken in allen Preisklassen anbieten, in verschiedenen Farben, auf Wunsch mit Grauanteil passend zum Alter des Trägers. Unsere Friseurmeisterin Frau Tiltrop berät Sie gerne, natürlich unverbindlich und kostenlos.

```html
<!DOCTYPE html>
<html lang="de">
<head>
<meta charset="utf-8">
<title>MOLVA Ketz – Zweithaar Studio Flyer</title>
<link href="https://fonts.googleapis.com/css2?family=Libre+Bodoni:wght@500&family=Arimo:wght@400&display=swap" rel="stylesheet">
<style>
:root{
  --stage:#a7a7a7;
  --brown-dark:#1f1a16;
  --slate:#25272a;
  --black:#0b0b0c;
  --wine:#2a0d0b;
  --paper:#ffffff;
  --text-light:#e8e4df;
  --text-soft:#cfc9c2;
  --text-dark:#222222;
  --serif:"Libre Bodoni", "Bodoni Moda", serif;
  --sans:"Arimo", "Helvetica Neue", Arial, sans-serif;
}
*{box-sizing:border-box;margin:0;padding:0}
html,body{width:1200px;height:3508px;overflow:hidden}
body{background:var(--stage);font-family:var(--sans);color:var(--text-light);position:relative}

.spread{position:absolute;left:69px;width:1062px;height:565px;display:flex;overflow:hidden}
.spread--outer{top:1144px}
.spread--inner{top:1799px}

/* outer spread: four panels */
.panel{position:relative;width:265.5px;height:100%;display:flex;flex-direction:column}
.panel__photo{height:350px;position:relative}
.panel__body{flex:1;padding:22px 24px}

.photo--man{background:linear-gradient(160deg,#2a2d36 0%,#1a1c24 45%,#0d0e12 100%)}
.photo--couple{background:radial-gradient(ellipse at 45% 45%,#5a3a2c 0%,#2b1c17 45%,#0f0c0b 100%)}
.photo--dark{background:linear-gradient(180deg,#15161a 0%,#101114 100%)}
.photo--woman{background:radial-gradient(ellipse at 55% 40%,#6a2218 0%,#2a0f0c 40%,#060505 80%)}

.body--brown{background:var(--brown-dark)}
.body--slate{background:var(--slate)}

.contact{background:var(--paper);color:var(--text-dark);display:flex;flex-direction:column;align-items:center;justify-content:center;text-align:center}
.contact__title{font-size:27px;margin-bottom:18px;font-weight:400}
.contact__line{font-size:11.5px;line-height:19px}
.contact__gap{height:10px}

.brand{display:flex;align-items:center;justify-content:center}
.brand__name{font-family:var(--serif);font-size:30px;color:var(--text-light);letter-spacing:1px}

.small-copy{font-size:12px;line-height:15.5px;color:var(--text-soft)}
.checklist{list-style:none;margin:10px 0 0 55px}
.checklist li{display:flex;align-items:center;gap:10px;font-size:16px;line-height:21.5px;color:var(--text-soft)}
.checklist svg{width:14px;height:14px;flex:none}

.question{text-align:center;display:flex;flex-direction:column;justify-content:center;align-items:center;padding-top:18px;padding-left:60px}
.question__lead{font-size:24px;line-height:30px}
.question__big{font-family:var(--serif);font-size:36px;line-height:40px;letter-spacing:2px}

.overlay-title{position:absolute;left:22px;bottom:20px}
.title-serif{font-family:var(--serif);font-size:37px;line-height:40px;letter-spacing:2px;color:var(--text-light)}
.title-sub{font-size:25px;line-height:30px;color:var(--text-light)}

.copy{font-size:16px;line-height:21px;color:var(--text-soft);text-align:justify}
.copy + .copy{margin-top:14px}

/* inner spread */
.half{width:531px;height:100%;position:relative;display:flex;flex-direction:column}
.why{background:var(--black);height:320px;display:flex;padding:34px 26px 0 24px;gap:48px}
.why__col{width:215px}
.why .title-serif{font-size:38px}
.why .title-sub{margin-left:4px}
.why__intro{margin-top:48px;font-size:16px;line-height:21px;color:var(--text-soft);text-align:justify}
.why__copy{font-size:12.5px;line-height:16px;color:var(--text-soft);text-align:justify}
.why__copy + .why__copy{margin-top:8px}

.faces{display:flex;height:245px}
.face{flex:1;border-right:2px solid var(--black)}
.face:last-child{border-right:0}
.face--a{background:linear-gradient(180deg,#3a2a22,#6b4a3a)}
.face--b{background:linear-gradient(180deg,#3d2c24,#7a5646)}
.face--c{background:linear-gradient(180deg,#2e211c,#5d3e30)}
.face--d{background:linear-gradient(180deg,#4a3a32,#9a7a66)}
.face--e{background:linear-gradient(180deg,#33302e,#6e6560)}
.face--f{background:linear-gradient(180deg,#2a1e19,#5a3e32)}

.wig-photo{height:310px;position:relative}
.wig-body{flex:1;background:var(--wine);display:flex;gap:40px;padding:16px 22px 0 24px}
.wig-col{width:215px}
.wig-lead{font-size:15.5px;line-height:20.5px;color:var(--text-soft);text-align:justify}
.wig-small{font-size:12.5px;line-height:16px;color:var(--text-soft);text-align:justify}
.wig-col .wig-small + .wig-small{margin-top:7px}
.wig-col .wig-lead + .wig-small{margin-top:22px}
</style>
</head>
<body>

<section class="spread spread--outer" aria-label="Außenseite">
  <div class="panel">
    <div class="panel__photo photo--man" role="img" aria-label="Foto: lächelnder Mann in dunkler Jacke, sitzend"></div>
    <div class="panel__body body--brown">
      <p class="small-copy">Dann sind Sie bei uns sehr gut aufgehoben, denn wir können Ihnen Ihr Toupet individuell auf Ihre Bedürfnisse hin anpassen:</p>
      <ul class="checklist">
        <li><svg viewBox="0 0 14 14"><circle cx="7" cy="7" r="6" fill="none" stroke="#cfc9c2"/><path d="M4 7.3l2 2 4-4.5" fill="none" stroke="#cfc9c2" stroke-width="1.3"/></svg>Farbe</li>
        <li><svg viewBox="0 0 14 14"><circle cx="7" cy="7" r="6" fill="none" stroke="#cfc9c2"/><path d="M4 7.3l2 2 4-4.5" fill="none" stroke="#cfc9c2" stroke-width="1.3"/></svg>Grauanteil</li>
        <li><svg viewBox="0 0 14 14"><circle cx="7" cy="7" r="6" fill="none" stroke="#cfc9c2"/><path d="M4 7.3l2 2 4-4.5" fill="none" stroke="#cfc9c2" stroke-width="1.3"/></svg>Größe</li>
        <li><svg viewBox="0 0 14 14"><circle cx="7" cy="7" r="6" fill="none" stroke="#cfc9c2"/><path d="M4 7.3l2 2 4-4.5" fill="none" stroke="#cfc9c2" stroke-width="1.3"/></svg>Styling</li>
      </ul>
    </div>
  </div>

  <div class="panel">
    <div class="panel__photo contact">
      <h2 class="contact__title">Kontakt</h2>
      <p class="contact__line">Inhaber Nachname</p>
      <p class="contact__line">Adresszeile 1</p>
      <p class="contact__line">1234 Adresse</p>
      <div class="contact__gap"></div>
      <p class="contact__line">Tel.: 0123 456 789</p>
      <p class="contact__line">info@molva-ketz.de</p>
      <p class="contact__line">www.molva-ketz.de</p>
    </div>
    <div class="panel__body body--slate brand">
      <span class="brand__name">MOLVA Ketz</span>
    </div>
  </div>

  <div class="panel">
    <div class="panel__photo photo--couple" role="img" aria-label="Foto: Paar, Frau mit langen Haaren und Mann im Anzug"></div>
    <div class="panel__body body--slate question">
      <p class="question__lead">Haben Sie</p>
      <p class="question__big">GENUG<br>HAARE</p>
      <p class="question__lead">gelassen?</p>
    </div>
  </div>

  <div class="panel">
    <div class="panel__photo photo--dark" role="img" aria-label="Dunkler Bildhintergrund">
      <div class="overlay-title">
        <h2 class="title-serif">TOUPETS</h2>
        <p class="title-sub">zum Wohlfühlen</p>
      </div>
    </div>
    <div class="panel__body body--brown">
      <p class="copy">Leiden Sie an übermäßigem Haarausfall?</p>
      <p class="copy">Fühlen Sie sich nicht mehr 100% wohl damit und möchten gerne wieder Ihre Attraktivität und vor allem das Wohlbefinden steigern?</p>
    </div>
  </div>
</section>

<section class="spread spread--inner" aria-label="Innenseite">
  <div class="half">
    <div class="why">
      <div class="why__col">
        <h2 class="title-serif">WARUM</h2>
        <p class="title-sub">bei uns kaufen?</p>
        <p class="why__intro">Mit unserer Befestigungsmethode sind Sie sehr flexibel - starker halt für jede Situation und auf Wunsch auch abnehmbar z.B. nachts beim schlafen.</p>
      </div>
      <div class="why__col">
        <p class="why__copy">Der große Vorteil unserer Befestigungsmethode liegt darin, dass Sie diese selbst umsetzen können und somit nicht jeden Monat das Studio zur Neubefestigung aufsuchen müssen. Das spart Ihnen Zeit und Geld.</p>
        <p class="why__copy">Wir können Ihnen Toupets und Perücken in allen Preisklassen anbieten, in verschiedenen Farben, auf Wunsch mit Grauanteil passend zum Alter des Trägers. Unsere Friseurmeisterin Frau Tiltrop berät Sie gerne, natürlich unverbindlich und kostenlos.</p>
      </div>
    </div>
    <div class="faces">
      <div class="face face--a" role="img" aria-label="Porträtfoto: lächelnder Mann"></div>
      <div class="face face--b" role="img" aria-label="Porträtfoto: lächelnde Frau"></div>
      <div class="face face--c" role="img" aria-label="Porträtfoto: lachender Mann"></div>
      <div class="face face--d" role="img" aria-label="Porträtfoto: lächelnde Frau"></div>
      <div class="face face--e" role="img" aria-label="Porträtfoto: lächelnder Mann"></div>
      <div class="face face--f" role="img" aria-label="Porträtfoto: lächelnde Frau"></div>
    </div>
  </div>

  <div class="half">
    <div class="wig-photo photo--woman" role="img" aria-label="Foto: Frau mit roten Haaren vor dunklem Hintergrund">
      <div class="overlay-title">
        <h2 class="title-serif">PERÜCKEN</h2>
        <p class="title-sub">für Natürlichkeit</p>
      </div>
    </div>
    <div class="wig-body">
      <div class="wig-col">
        <p class="wig-lead">Sind Sie an einer Perücke interessiert die augenscheinlich keinen Unterschied zu gewachsenem Haar aufweist?</p>
        <p class="wig-small">Dann sind Sie bei uns an der richtigen Adresse. Die langjährige Erfahrung im Zweithaar Bereich von Friseurmeisterin Greta Tiltrop verspricht Ihnen optimale Beratung</p>
      </div>
      <div class="wig-col">
        <p class="wig-small">und ein individuell auf Sie abgestimmtes Produkt.</p>
        <p class="wig-small">Bei uns erhalten Sie Zugriff auf verschiedene Modelle im gesamten Preisspektrum.</p>
        <p class="wig-small">Liegt eine von Ihrem Arzt attestierte Erkrankung vor, übernimmt Ihre Krankenkasse höchstwahrscheinlich die Kosten für Ihr Zweithaar. Die Formalitäten dazu erledigen wir gerne für Sie um Ihnen unnötigen Stress zu ersparen.</p>
      </div>
    </div>
  </div>
</section>

</body>
</html>
```